Ringbeacon Hub - Web design / template design

Hello,

I need a design for my existing site. I already have a logo that I want to use, which you can find on my site ( I can also provide different formats / larger versions ).

Please see http://www.ringbeaconhub.example for details of the site.

What I need are pages with sections that can be edited, so for example, I need basic table / div content sections that I can place in the members area that can contain whatever custom content I need to put in them without the table / div design getting stretched out or skewed.

The main page, basically needs to have all of the content on the current page or room for it at least should I want to add it.

You can also see ww2.ringbeaconhub.example with more info ( not a live site and me trying my best to do something, but I'm just not good at design :)

The site content for the most part needs to be actual text, rather than text on images. I will need to change this content and have it indexed by search engines, if you want, you can just put filler text in. There are exceptions of course, like maybe on the main page, if there are boxes with some static image text, that is fine.

Target Market(s)

Telephony, phone service providers, phone system users

Industry/Entity Type

It Service

Requirements
Must have
• Dynamic content capabilities.

Logo colors implemented in the site in some way.

Easy navigation ( tabs at the top are good or whatever you think ).

I will have the following sections:

1. Home
2. About us ( company info ).
3. How to / Help
4. Pricing
5. Support section.
6. Contact section
7. Singup section
8. Members section

I would like the main page to be more image / wow factor and the other pages really just need to be basic layout and places to put tables or divs with content in them. Table or div header images are for titles are ok as long as I can edit them.

Nice to have
• Sign up button placed somewhere.

Twitter / Facebook / LinkedIn buttons

Should not have
• Flash or all page content in static images.

```html
<!DOCTYPE html>
<html lang="en">
<head>
<meta charset="utf-8">
<title>Ringbeacon Hub – CNAM Provider</title>
<link href="https://fonts.googleapis.com/css2?family=Noto+Sans:wght@400;700&family=Oswald:wght@300;400&display=swap" rel="stylesheet">
<style>
:root{
  --page:#f1f1f1;
  --white:#ffffff;
  --blue:#0a6fbd;
  --blue-dark:#075a9e;
  --blue-light:#3f9be0;
  --nav:#1f6fb0;
  --green:#2f9a12;
  --green-dark:#1b6e06;
  --text:#3a3a3a;
  --line:#dcdcdc;
  --title-blue:#1d5fa6;
}
*{box-sizing:border-box;margin:0;padding:0}
html,body{width:993px;height:1200px;overflow:hidden}
body{background:var(--page);font-family:"Noto Sans",Verdana,sans-serif;color:var(--text);position:relative}
.abs{position:absolute}

.site-header{left:0;top:0;width:993px;height:99px;background:var(--white);border-bottom:2px solid #e2e2e2}
.brand{left:108px;top:40px;display:flex;align-items:center;gap:8px;font-size:24px;font-weight:700;color:var(--blue)}
.brand-mark{width:14px;height:14px;border-radius:50%;background:var(--green)}
.main-nav{top:57px;left:0;width:993px;font-size:12px;color:var(--nav)}
.main-nav a{position:absolute;color:inherit;text-decoration:none;white-space:nowrap}

.intro{left:0;top:101px;width:993px;height:88px;text-align:center}
.intro h1{font-family:"Oswald",sans-serif;font-weight:300;font-size:17.5px;color:var(--green);margin-top:14px;letter-spacing:.1px}
.intro p{font-size:8px;font-weight:700;color:#222;width:500px;margin:8px auto 0;line-height:12.5px}

.feature-band{left:0;top:189px;width:993px;height:269px;
  background:radial-gradient(ellipse 300px 220px at 496px 110px,#5fb1ea 0%,rgba(63,155,224,.4) 45%,rgba(10,111,189,0) 100%),linear-gradient(#0d79c6,#0a69b4)}
.feature{top:24px;width:224px;color:#fff}
.feature h2{font-size:13px;font-weight:400;letter-spacing:.3px}
.feature p{font-size:10px;line-height:12.4px;text-align:justify;margin-top:12px;letter-spacing:.2px}
.feature p + p{margin-top:11px}
.btn{display:inline-block;background:#fff;border:1px solid #c9d3dc;border-radius:3px;font-size:10px;color:var(--nav);padding:4px 0;width:76px;text-align:center;text-decoration:none}
.feature .btn{position:absolute;right:0;top:202px}

.panel{background:var(--white);border:1px solid var(--line);border-radius:5px}
.intro-panel{left:104px;top:470px;width:786px;height:201px;padding:17px 23px}
.intro-panel h3{font-size:12.5px;font-weight:400;color:var(--title-blue);letter-spacing:.4px}
.intro-panel p{font-size:10px;line-height:15px;text-align:justify;margin-top:10px;letter-spacing:.1px}
.intro-panel p + p{margin-top:7px}

.card{top:683px;width:221px;height:155px}
.card-icon{left:18px;top:34px;width:54px;height:54px}
.card h4{position:absolute;left:91px;top:12px;font-size:15px;font-weight:400;color:var(--green)}
.card p{position:absolute;left:91px;top:42px;width:108px;font-size:10px;line-height:12.5px;text-align:justify}
.card .btn{position:absolute;left:90px;top:124px}

.list-panel{left:104px;top:850px;width:786px;height:284px}
.list-col{top:13px;width:181px}
.list-col h5{height:30px;line-height:30px;background:linear-gradient(#3b8be0,#1661c2);color:#fff;font-size:12.5px;font-weight:400;padding-left:17px;letter-spacing:.4px;border-radius:1px}
.list-col ul{list-style:none;margin-top:11px;padding-left:10px}
.list-col li{font-size:10px;line-height:18.4px;padding-left:13px;position:relative;letter-spacing:.3px}
.list-col li::before{content:"";position:absolute;left:0;top:6px;width:5px;height:5px;background:var(--green-dark)}

.social{top:1151px;width:27px;height:27px;border-radius:3px;border:1px solid #8fb0cc;background:linear-gradient(#5aa6e3,#1f69b0)}
.copyright{right:103px;top:1162px;font-size:8.5px;color:var(--green-dark);letter-spacing:.3px}
</style>
</head>
<body>

<header class="abs site-header">
  <div class="abs brand"><span class="brand-mark"></span>Ringbeacon Hub</div>
  <nav class="abs main-nav">
    <a href="#" style="left:445px">Home</a>
    <a href="#" style="left:530px">About us</a>
    <a href="#" style="left:633px">CNAM Help</a>
    <a href="#" style="left:748px">Pricing</a>
    <a href="#" style="left:837px">Sing Up</a>
  </nav>
</header>

<section class="abs intro">
  <h1>CNAM Provider For VoIP Based Phone Systems - Get Caller Name On Your Inbound VoIP Calls</h1>
  <p>Welcome to RingbeaconHub.example. It is a long established fact that a reader will be distracted by the readable content of a page when looking at its layout. The point of using Lorem .</p>
</section>

<section class="abs feature-band">
  <article class="abs feature" style="left:113px">
    <h2>About RingbeaconHub.example</h2>
    <p>RingbeaconHub.example is a leading provider of CNAM / Caller ID Name services for VoIP providers and PBX systems. We support United States and Canadian phone numbers.</p>
    <p>We have access to all of the major CNAM databases in the United States and Canada, something we're proud to offer.</p>
    <p>Use our easy to use examples to begin delivering caller ID name to your PBX or VoIP customers in minutes.</p>
    <a class="btn" href="#">Read More</a>
  </article>
  <article class="abs feature" style="left:376px">
    <h2>What is CNAM?</h2>
    <p>RingbeaconHub.example is a leading provider of CNAM / Caller ID Name services for VoIP providers and PBX systems. We support United States and Canadian phone numbers.</p>
    <p>We have access to all of the major CNAM databases in the United States and Canada, something we're proud to offer.</p>
    <p>Use our easy to use examples to begin delivering caller ID name to your PBX or VoIP customers in minutes.</p>
    <a class="btn" href="#">Read More</a>
  </article>
  <article class="abs feature" style="left:635px">
    <h2>How can RingbeaconHub.example Help?</h2>
    <p>RingbeaconHub.example is a leading provider of CNAM / Caller ID Name services for VoIP providers and PBX systems. We support United States and Canadian phone numbers.</p>
    <p>We have access to all of the major CNAM databases in the United States and Canada, something we're proud to offer.</p>
    <p>Use our easy to use examples to begin delivering caller ID name to your PBX or VoIP customers in minutes.</p>
    <a class="btn" href="#">Read More</a>
  </article>
</section>

<section class="abs panel intro-panel">
  <h3>Lorem Ipsum is simply dummy text</h3>
  <p>It is a long established fact that a reader will be distracted by the readable content of a page when looking at its layout. The point of using Lorem Ipsum is that it has a more-or-less normal distribution of letters, as opposed to using 'Content here, content here', making it look like readable English. Many desktop publishing packages and web page editors now use Lorem Ipsum as their default model text, and a search for 'lorem ipsum' will uncover many web sites still in their infancy.</p>
  <p>It is a long established fact that a reader will be distracted by the readable content of a page when looking at its layout. The point of using Lorem Ipsum is that it has a more-or-less normal distribution of letters, as opposed to using 'Content here, content here', making it look like readable English. Many desktop publishing packages.istribution of letters, as opposed to using 'Content here, content here', making it look like readable English. Many desktop publishing packages.</p>
</section>

<article class="abs panel card" style="left:147px">
  <div class="abs card-icon" role="img" aria-label="Support illustration of two users" style="border-radius:12px;background:linear-gradient(135deg,#8fe07a,#3a7fd0)"></div>
  <h4>Support</h4>
  <p>Contrary to popular belief, Lorem Ipsum is not simply random text.Lorem Ipsum is not simply random text.</p>
  <a class="btn" href="#">Read More</a>
</article>
<article class="abs panel card" style="left:385px">
  <svg class="abs card-icon" viewBox="0 0 54 54" aria-hidden="true">
    <circle cx="27" cy="27" r="26" fill="#2a93d6"/>
    <circle cx="27" cy="27" r="22" fill="#47aee6"/>
    <path d="M20 15c2-1 4 0 5 2l1 5c0 1-1 2-2 3 1 4 3 7 6 9 1-1 2-2 3-1l5 2c2 1 2 3 1 5l-2 2c-8 1-19-12-18-22z" fill="#fff"/>
  </svg>
  <h4>Contact Us</h4>
  <p>Contrary to popular belief, Lorem Ipsum is not simply random text.Lorem Ipsum is not simply random text.</p>
  <a class="btn" href="#">Read More</a>
</article>
<article class="abs panel card" style="left:621px">
  <div class="abs card-icon" role="img" aria-label="Padlock and key illustration" style="border-radius:10px;background:linear-gradient(135deg,#d9c98a,#8b7a3e)"></div>
  <h4>Members Login</h4>
  <p>Contrary to popular belief, Lorem Ipsum is not simply random text.Lorem Ipsum is not simply random text.</p>
  <a class="btn" href="#">Read More</a>
</article>

<section class="abs panel list-panel">
  <div class="abs list-col" style="left:9px">
    <h5>Why RingbeaconHub?</h5>
    <ul><li>Realtime CNAM Dips.</li><li>No Monthly Fees.</li><li>Low Query Rates.</li><li>Free Support.</li><li>U.S. and Canadian CNAM</li><li>No Account Minimums.</li><li>Integration Assistance.</li><li>Extensive Compatablity.</li><li>High Quality Results.</li><li>Automatic Volume Discounts.</li><li>10 Daily CNAM updates.</li><li>Free, Instant Account Setup.</li></ul>
  </div>
  <div class="abs list-col" style="left:202px">
    <h5>Compatability</h5>
    <ul><li>Realtime CNAM Dips.</li><li>No Monthly Fees.</li><li>Low Query Rates.</li><li>Free Support.</li><li>U.S. and Canadian CNAM</li><li>No Account Minimums.</li><li>Integration Assistance.</li><li>Extensive Compatablity.</li><li>High Quality Results.</li><li>Automatic Volume Discounts.</li><li>10 Daily CNAM updates.</li><li>Free, Instant Account Setup.</li></ul>
  </div>
  <div class="abs list-col" style="left:396px">
    <h5>Quality and Service</h5>
    <ul><li>Realtime CNAM Dips.</li><li>No Monthly Fees.</li><li>Low Query Rates.</li><li>Free Support.</li><li>U.S. and Canadian CNAM</li><li>No Account Minimums.</li><li>Integration Assistance.</li><li>Extensive Compatablity.</li><li>High Quality Results.</li><li>Automatic Volume Discounts.</li><li>10 Daily CNAM updates.</li><li>Free, Instant Account Setup.</li></ul>
  </div>
  <div class="abs list-col" style="left:591px">
    <h5>Implementation Help</h5>
    <ul><li>Realtime CNAM Dips.</li><li>No Monthly Fees.</li><li>Low Query Rates.</li><li>Free Support.</li><li>U.S. and Canadian CNAM</li><li>No Account Minimums.</li><li>Integration Assistance.</li><li>Extensive Compatablity.</li><li>High Quality Results.</li><li>Automatic Volume Discounts.</li><li>10 Daily CNAM updates.</li><li>Free, Instant Account Setup.</li></ul>
  </div>
</section>

<footer>
  <a class="abs social" href="#" aria-label="Social profile one" style="left:112px"></a>
  <a class="abs social" href="#" aria-label="Social profile two" style="left:146px"></a>
  <a class="abs social" href="#" aria-label="Social profile three" style="left:180px"></a>
  <p class="abs copyright">[ Copyright 2011 RingbeaconHub.example | Brought to you by NorthWire ]</p>
</footer>

</body>
</html>
```